Quorvilan Mobile App

We are in need of a design for a mobile application that delivers relevant content to users based on the profile that they enter and based on the answers that they enter in a daily health tracker. There also will be functionality that will allow a user to check the cost of a medical service/ procedure before going to the medical provider (could get a list of providers and costs after entering procedure, service or prescription in a search box). The content will be articles or information that our team will find/develop on a daily basis and put into a database that the app will pull off of. The profile needs to capture age, sex, ethinicity (optional) and then have a list of topics that the user can select to get daily updated information/content. These topics are: Diabetes, Heart Disease, Hypertension, COPD, Back Pain, Weight Management, Depression, Cancer, Wellness Plan. The final design should allow for users to receive helpful health care information every day based on their profile and the answers in the daily health tracker.

Medical

```html
<!DOCTYPE html>
<html lang="en">
<head>
<meta charset="utf-8">
<title>Quorvilan – Daily Health Tracker</title>
<link href="https://fonts.googleapis.com/css2?family=Crete+Round&family=Roboto:wght@400;500&display=swap" rel="stylesheet">
<style>
  :root {
    --canvas: #f2f4f6;
    --status-bg: #eef4f8;
    --header-bg: #eaf3f8;
    --ink: #222a30;
    --brand: #3aa6d4;
    --band: #2a9bc5;
    --sky: #34afd9;
    --divider: rgba(10, 90, 130, 0.16);
    --label: #e9f7fc;
    --lead: #1d5f78;
    --white: #ffffff;
    --go-top: #86c866;
    --go-bottom: #62ab43;
    --go-edge: #55973a;
  }
  * { box-sizing: border-box; margin: 0; padding: 0; }
  html, body { width: 1024px; height: 1200px; overflow: hidden; }
  body { background: var(--canvas); font-family: "Roboto", Helvetica, sans-serif; }

  .app-screen {
    position: absolute; left: 172px; top: 0;
    width: 680px; height: 1200px;
    background: var(--sky);
    display: flex; flex-direction: column;
  }

  .status-bar {
    height: 52px; background: var(--status-bg); color: var(--ink);
    display: flex; align-items: center; justify-content: space-between;
    padding: 0 14px; font-size: 22px;
  }
  .status-left, .status-right { display: flex; align-items: center; gap: 8px; }
  .signal { display: flex; gap: 3px; }
  .signal i { width: 11px; height: 11px; border-radius: 50%; background: var(--ink); display: block; }

  .nav-header {
    height: 86px; background: var(--header-bg); position: relative;
    display: flex; align-items: center; justify-content: center;
  }
  .back-button {
    position: absolute; left: 22px; top: 18px;
    display: flex; align-items: center;
    font-family: "Crete Round", Georgia, serif; font-size: 25px; color: var(--brand);
  }
  .back-button svg { position: absolute; left: 0; top: 0; }
  .back-button span { position: relative; padding: 10px 14px 0 30px; height: 54px; }
  .brand-name {
    display: flex; align-items: center; gap: 10px;
    font-family: "Crete Round", Georgia, serif; font-size: 29px; color: var(--brand);
  }
  .brand-mark { width: 20px; height: 20px; background: var(--brand); display: block; }

  .intro-band {
    height: 84px; background: var(--band); color: var(--white);
    padding: 16px 38px 0; font-size: 18px; line-height: 27px;
  }
  .intro-band strong { font-family: "Crete Round", Georgia, serif; font-weight: 400; color: var(--lead); }

  .question {
    height: 112px; border-bottom: 1px solid var(--divider);
    padding: 20px 38px 0;
  }
  .question-label {
    font-family: "Crete Round", Georgia, serif; font-size: 21px; color: var(--label);
  }
  .choices { display: flex; margin-top: 16px; }
  .choice { display: flex; align-items: center; gap: 16px; color: var(--white); font-size: 19px; }
  .choices.two .choice { width: 302px; }
  .choices.three .choice:nth-child(1) { width: 198px; }
  .choices.three .choice:nth-child(2) { width: 184px; }
  .radio {
    width: 34px; height: 34px; border: 3px solid var(--white); border-radius: 50%;
    display: flex; align-items: center; justify-content: center; flex: none;
  }
  .radio.is-selected::after {
    content: ""; width: 11px; height: 11px; border-radius: 50%; background: var(--white);
  }

  .result-entry { display: flex; align-items: center; gap: 14px; margin-top: 12px; color: var(--white); font-size: 18px; }
  .result-field {
    width: 218px; height: 50px; background: var(--white);
    padding: 14px 16px; color: var(--brand); font-size: 16px; font-weight: 500;
  }

  .submit-area { flex: 1; padding: 30px 24px 0; }
  .submit-button {
    height: 114px; border-radius: 6px;
    background: linear-gradient(var(--go-top), var(--go-bottom));
    border: 1px solid var(--go-edge);
    display: flex; align-items: center; justify-content: center;
    font-family: "Crete Round", Georgia, serif; font-size: 40px; color: var(--white);
  }
</style>
</head>
<body>
<main class="app-screen">

  <header class="status-bar">
    <div class="status-left">
      <span class="signal"><i></i><i></i><i></i><i></i><i></i></span>
      <span>Nettra</span>
      <svg width="24" height="18" viewBox="0 0 24 18" aria-hidden="true">
        <path d="M2 6a14 14 0 0 1 20 0" fill="none" stroke="#222a30" stroke-width="2.6"/>
        <path d="M6 10a8.5 8.5 0 0 1 12 0" fill="none" stroke="#222a30" stroke-width="2.6"/>
        <circle cx="12" cy="15" r="2.4" fill="#222a30"/>
      </svg>
    </div>
    <div class="status-time">9:23 AM</div>
    <div class="status-right">
      <svg width="20" height="20" viewBox="0 0 20 20" aria-hidden="true"><path d="M18 2 2 9l7 2 2 7z" fill="#222a30"/></svg>
      <span>66%</span>
      <svg width="50" height="22" viewBox="0 0 50 22" aria-hidden="true">
        <rect x="1" y="2" width="44" height="18" rx="3" fill="none" stroke="#222a30" stroke-width="2"/>
        <rect x="4" y="5" width="26" height="12" fill="#222a30"/>
        <rect x="46" y="8" width="3" height="6" fill="#222a30"/>
      </svg>
    </div>
  </header>

  <nav class="nav-header">
    <div class="back-button">
      <svg width="102" height="54" viewBox="0 0 102 54" aria-hidden="true">
        <path d="M20 2H96a4 4 0 0 1 4 4V48a4 4 0 0 1-4 4H20L2 27z" fill="none" stroke="#3aa6d4" stroke-width="2"/>
      </svg>
      <span>Back</span>
    </div>
    <div class="brand-name"><i class="brand-mark"></i>Quorvilan</div>
  </nav>

  <section class="intro-band">
    <p><strong>Health Care Connected.</strong> This is your personal health tracker. Keep a record of your healthy behaviors and access the history anytime.</p>
  </section>

  <section class="question">
    <p class="question-label">How many hours did you sleep last night?</p>
    <div class="choices two">
      <label class="choice"><span class="radio is-selected"></span>Less than 6 hours</label>
      <label class="choice"><span class="radio"></span>More than 6 hours</label>
    </div>
  </section>

  <section class="question">
    <p class="question-label">Have you exercised today?</p>
    <div class="choices two">
      <label class="choice"><span class="radio is-selected"></span>Yes</label>
      <label class="choice"><span class="radio"></span>No</label>
    </div>
  </section>

  <section class="question">
    <p class="question-label">Have you had a cigarette today?</p>
    <div class="choices two">
      <label class="choice"><span class="radio is-selected"></span>Yes</label>
      <label class="choice"><span class="radio"></span>No</label>
    </div>
  </section>

  <section class="question">
    <p class="question-label">Have you had any alcoholic beverages today?</p>
    <div class="choices two">
      <label class="choice"><span class="radio is-selected"></span>Yes</label>
      <label class="choice"><span class="radio"></span>No</label>
    </div>
  </section>

  <section class="question">
    <p class="question-label">How would you describe your eating over the last 24 hrs?</p>
    <div class="choices three">
      <label class="choice"><span class="radio is-selected"></span>Healthy</label>
      <label class="choice"><span class="radio"></span>Not bad</label>
      <label class="choice"><span class="radio"></span>Needs improvement</label>
    </div>
  </section>

  <section class="question">
    <p class="question-label">How would you describe your stress level over the last 24 hrs?</p>
    <div class="choices three">
      <label class="choice"><span class="radio is-selected"></span>Healthy</label>
      <label class="choice"><span class="radio"></span>Not bad</label>
      <label class="choice"><span class="radio"></span>Needs improvement</label>
    </div>
  </section>

  <section class="question">
    <p class="question-label">Have you checked your insulin levels today?</p>
    <div class="result-entry">
      <span>If yes, enter results here:</span>
      <span class="result-field">#</span>
    </div>
  </section>

  <div class="submit-area">
    <div class="submit-button">Submit to your Health Tracker</div>
  </div>

</main>
</body>
</html>
```